Insight Plus. needs Business Cards

For this project, we need business cards (currently have also put a call out for a logo). We are a start-up called Insight Plus. This is our second company (our first one was called Querivance). Traditionally we have been providing market research services across different sectors, primarily financial services and the pharmaceutical industry. However, we now want to go beyond market research to offer more (Plus.)... strategic consulting and big data knowledge management. We want our brand to be approachable, creative, fun but professional.

Target Market(s)

The target audience is a business professional - we are B2B (business to business) and do not sell our services to individuals. The brands we work with are major brands across industries, but primarily automotive, financial and pharmaceutical.

Industry/Entity Type

Market Research

Font styles to use
Serif
Sans Serif
Other font styles liked:
• Calibri

Requirements
Must have
• Be clean, simple, modern
Show our address and phone number and email address and website URL
We do not need to have titles showing.

```html
<!DOCTYPE html>
<html lang="en">
<head>
<meta charset="utf-8">
<title>Insight Plus. Business Cards</title>
<link rel="stylesheet" href="https://fonts.googleapis.com/css2?family=Roboto:wght@300;400&display=swap">
<style>
  :root {
    --bg: #e6e2dc;
    --card: #ffffff;
    --blue: #2f5b9c;
    --blue-soft: #5b82b8;
    --shadow: rgba(40, 30, 20, 0.25);
  }
  * { margin: 0; padding: 0; box-sizing: border-box; }
  html, body { width: 1200px; height: 858px; overflow: hidden; }
  body {
    background: var(--bg);
    font-family: "Roboto", Arial, sans-serif;
    color: var(--blue);
    position: relative;
  }
  .card {
    position: absolute;
    width: 540px;
    height: 309px;
    background: var(--card);
    box-shadow: 0 6px 18px var(--shadow);
    overflow: hidden;
  }
  .card--front { left: 40px; top: 275px; }
  .card--back { left: 620px; top: 275px; }

  .wordmark {
    display: flex;
    align-items: center;
    gap: 10px;
    font-weight: 400;
    color: var(--blue);
    white-space: nowrap;
  }
  .wordmark__square {
    width: 12px; height: 12px;
    background: var(--blue);
  }
  .card--front .wordmark {
    position: absolute; left: 38px; top: 42px;
    font-size: 34px;
  }
  .card--back .wordmark {
    position: absolute; left: 50%; top: 50%;
    transform: translate(-50%, -50%);
    font-size: 38px;
  }

  .person { position: absolute; left: 38px; top: 124px; }
  .person__name { font-size: 22px; font-weight: 300; }
  .person__role { font-size: 12px; font-weight: 300; color: var(--blue-soft); margin-top: 2px; }

  .divider {
    position: absolute; left: 236px; right: 0; top: 151px;
    height: 1px; background: var(--blue);
  }

  .website {
    position: absolute; right: 40px; top: 36px;
    font-size: 12px; font-weight: 300; color: var(--blue-soft);
  }

  .contact {
    position: absolute; left: 38px; top: 222px;
    font-size: 12px; font-weight: 300; color: var(--blue-soft);
    display: grid; gap: 7px;
  }
  .contact__row, .address { display: flex; align-items: center; gap: 8px; }
  .icon { width: 12px; height: 12px; fill: var(--blue); flex: none; }

  .address {
    position: absolute; right: 40px; top: 176px;
    font-size: 12px; font-weight: 300; color: var(--blue-soft);
    align-items: flex-start;
  }
  .address .icon { margin-top: 2px; }
  .address__lines { line-height: 1.35; }

  .band {
    position: absolute; left: 0; right: 0; bottom: 0;
    height: 26px; background: var(--blue);
  }
</style>
</head>
<body>
  <section class="card card--front" aria-label="Business card front">
    <div class="wordmark"><span class="wordmark__square"></span>Insight Plus.</div>
    <div class="website">www.insightplus.example</div>
    <div class="person">
      <div class="person__name">Employee Name</div>
      <div class="person__role">Managing Director</div>
    </div>
    <div class="divider"></div>
    <div class="address">
      <svg class="icon" viewBox="0 0 12 12" aria-hidden="true"><path d="M6 1 L11.5 6 H10 V11 H7.2 V7.8 H4.8 V11 H2 V6 H0.5 Z"/></svg>
      <div class="address__lines">Insight Plus Ltd 14 Harbour Row<br>Millbrook NY 10010</div>
    </div>
    <div class="contact">
      <div class="contact__row">
        <svg class="icon" viewBox="0 0 12 12" aria-hidden="true"><circle cx="6" cy="3.5" r="2.6"/><path d="M1 12 C1 8 3 6.8 6 6.8 C9 6.8 11 8 11 12 Z"/></svg>
        <span>0044 5612 870</span>
      </div>
      <div class="contact__row">
        <svg class="icon" viewBox="0 0 12 12" aria-hidden="true"><path d="M0.5 2 H11.5 V10 H0.5 Z M1.5 3 L6 6.6 L10.5 3 Z" fill-rule="evenodd"/></svg>
        <span>hello@insightplus.example</span>
      </div>
    </div>
    <div class="band"></div>
  </section>

  <section class="card card--back" aria-label="Business card back">
    <div class="wordmark"><span class="wordmark__square"></span>Insight Plus.</div>
  </section>
</body>
</html>
```